Copper Ridge Business Cards For New Startup

I am looking for you to design some business cards for a new startup https://copperridgehub.example. I have supplied logo, brand guidelines and our signatures as a guide.

We need this to reflect the brand guidelines and the website for brand consistency,

What is Copper Ridge?

Mallorca's Business Growth Community
Join your new business community full of passionate entrepreneurs who
love to solve problems and help each other grow together!

Any questions you can ask.

Target Market(s)

Business to Business

Contact Information for Business Card

These are attached (signatures) to the job

Font styles to use
Other font styles liked:
• Open Sans

Requirements
Must have
• Match design guidelines
Nice to have
• Photos of our faces so people remember us

```html
<!DOCTYPE html>
<html lang="en">
<head>
<meta charset="utf-8">
<title>Copper Ridge Business Cards</title>
<link href="https://fonts.googleapis.com/css2?family=Open+Sans:wght@300;400;600&display=swap" rel="stylesheet">
<style>
  :root {
    --brand: #676500;
    --white: #ffffff;
    --page: #ffffff;
    --edge: #d9d9d9;
    --photo-light: #d8c9bb;
    --photo-dark: #7d6a5c;
  }
  * { box-sizing: border-box; margin: 0; padding: 0; }
  html, body { width: 1200px; height: 1000px; overflow: hidden; background: var(--page); }
  body { position: relative; font-family: "Open Sans", Arial, sans-serif; }

  .card {
    position: absolute;
    width: 462px;
    height: 264px;
    border-radius: 30px;
    overflow: hidden;
  }
  .card--front { left: 116px; background: var(--brand); }
  .card--back { left: 623px; background: var(--white); border: 1px solid var(--edge); }
  .row-1 { top: 215px; }
  .row-2 { top: 522px; }

  .front-brand {
    position: absolute;
    left: 0; top: 52px;
    width: 254px;
    text-align: center;
    color: var(--white);
  }
  .front-brand .brand-ring {
    display: block;
    margin: 0 auto 12px;
    width: 120px; height: 120px;
    border: 5px solid var(--white);
    border-radius: 50%;
  }
  .front-brand .brand-name {
    font-size: 20px; font-weight: 600; letter-spacing: 0.5px; text-transform: uppercase;
  }

  .portrait {
    position: absolute;
    inset: 0;
    clip-path: polygon(304px 0, 100% 0, 100% 100%, 212px 100%);
  }
  .portrait--man { background: linear-gradient(160deg, #e9e6df 0%, #bfa898 45%, #3e4d66 100%); }
  .portrait--woman { background: linear-gradient(160deg, var(--photo-light) 0%, #e8c7ad 50%, #a88466 100%); }

  .back-brand {
    position: absolute;
    left: 40px; top: 38px;
    width: 140px;
    text-align: center;
    color: var(--brand);
  }
  .back-brand .brand-ring {
    display: block;
    margin: 0 auto 8px;
    width: 94px; height: 94px;
    border: 4px solid var(--brand);
    border-radius: 50%;
  }
  .back-brand .brand-name {
    font-size: 16px; font-weight: 600; letter-spacing: 0.3px; text-transform: uppercase; white-space: nowrap;
  }

  .person {
    position: absolute;
    left: 237px; top: 42px;
    color: var(--brand);
  }
  .person .name { font-size: 20px; font-weight: 600; letter-spacing: -0.5px; line-height: 26px; }
  .person .role { font-size: 16px; font-weight: 300; line-height: 20px; }
  .person .contacts { list-style: none; margin-top: 16px; font-size: 14px; line-height: 22px; }
  .person .contacts li { display: flex; align-items: center; gap: 6px; }
  .person .contacts svg { width: 14px; height: 12px; fill: var(--brand); }

  .footer-band { position: absolute; left: 0; bottom: 0; width: 462px; height: 90px; }
  .footer-band svg.band { position: absolute; inset: 0; }
  .footer-band .site {
    position: absolute; left: 0; right: 0; top: 17px;
    text-align: center; color: var(--white); font-size: 14px; font-weight: 600;
  }
  .footer-band .social {
    position: absolute; left: 153px; top: 41px;
    display: flex; gap: 5px; list-style: none;
  }
  .footer-band .social li {
    width: 26px; height: 26px; border: 1.5px solid var(--white); border-radius: 50%;
  }
</style>
</head>
<body>

  <!-- Card 1 front -->
  <section class="card card--front row-1">
    <div class="front-brand">
      <span class="brand-ring"></span>
      <span class="brand-name">Copper Ridge</span>
    </div>
    <div class="portrait portrait--man" role="img" aria-label="Portrait photo of Daniel Marsh"></div>
  </section>

  <!-- Card 1 back -->
  <section class="card card--back row-1">
    <div class="back-brand">
      <span class="brand-ring"></span>
      <span class="brand-name">Copper Ridge</span>
    </div>
    <div class="person">
      <p class="name">Daniel Marsh</p>
      <p class="role">Founder &amp; Growth Hacker</p>
      <ul class="contacts">
        <li><svg viewBox="0 0 14 12"><path d="M1 3 Q7 -1 13 3 L11 5 L9 3.5 L5 3.5 L3 5 Z M3 6 L11 6 L13 11 L1 11 Z"/></svg>+34 600 555 018</li>
        <li><svg viewBox="0 0 14 12"><path d="M1 2 H13 V10 H1 Z" fill="none" stroke="currentColor"/><path d="M1 2 H13 V10 H1 Z M2 3 L7 7 L12 3"/></svg>dm@copperridgehub.example</li>
      </ul>
    </div>
    <div class="footer-band">
      <svg class="band" viewBox="0 0 462 90" preserveAspectRatio="none"><path d="M0 25 Q231 -14 462 25 V90 H0 Z" fill="var(--brand)"/></svg>
      <p class="site">copperridgehub.example</p>
      <ul class="social"><li></li><li></li><li></li><li></li><li></li></ul>
    </div>
  </section>

  <!-- Card 2 front -->
  <section class="card card--front row-2">
    <div class="front-brand">
      <span class="brand-ring"></span>
      <span class="brand-name">Copper Ridge</span>
    </div>
    <div class="portrait portrait--woman" role="img" aria-label="Portrait photo of Helen Whitford"></div>
  </section>

  <!-- Card 2 back -->
  <section class="card card--back row-2">
    <div class="back-brand">
      <span class="brand-ring"></span>
      <span class="brand-name">Copper Ridge</span>
    </div>
    <div class="person">
      <p class="name">Helen Whitford</p>
      <p class="role">Relationship Director</p>
      <ul class="contacts">
        <li><svg viewBox="0 0 14 12"><path d="M1 3 Q7 -1 13 3 L11 5 L9 3.5 L5 3.5 L3 5 Z M3 6 L11 6 L13 11 L1 11 Z"/></svg>+44 7700 900 412</li>
        <li><svg viewBox="0 0 14 12"><path d="M1 2 H13 V10 H1 Z M2 3 L7 7 L12 3"/></svg>hw@copperridgehub.example</li>
      </ul>
    </div>
    <div class="footer-band">
      <svg class="band" viewBox="0 0 462 90" preserveAspectRatio="none"><path d="M0 25 Q231 -14 462 25 V90 H0 Z" fill="var(--brand)"/></svg>
      <p class="site">copperridgehub.example</p>
      <ul class="social"><li></li><li></li><li></li><li></li><li></li></ul>
    </div>
  </section>

</body>
</html>
```